Plastic Rubber & Vinyl Trim

We need a couple new products for our car care line going into next year. One of the new products we are considering is a Trim restorer for the exterior trim, rubber moldings, and vinyl.

```html
<!DOCTYPE html>
<html lang="en">
<head>
<meta charset="utf-8">
<title>Trim Restorer Label</title>
<link rel="stylesheet" href="https://fonts.googleapis.com/css2?family=Anton&family=Kanit:ital,wght@1,700;1,800&family=Oswald:wght@500;700&display=swap">
<style>
  :root {
    --page: #ffffff;
    --navy: #1d1f6e;
    --deep: #0b1a4a;
    --teal: #2aa8c9;
    --cyan: #6fd6ee;
    --white: #ffffff;
    --silver-light: #f4f5f7;
    --silver-mid: #c9ccd2;
    --ink: #0c0c0f;
  }
  * { margin: 0; padding: 0; box-sizing: border-box; }
  html, body { width: 1200px; height: 1200px; overflow: hidden; background: var(--page); }
  .label {
    position: absolute; left: 369px; top: 54px; width: 462px; height: 1092px;
    overflow: hidden; font-family: "Kanit", sans-serif; color: var(--white);
  }
  .label__art {
    position: absolute; inset: 0;
    background:
      radial-gradient(ellipse at 70% 25%, rgba(111,214,238,.55), transparent 55%),
      radial-gradient(ellipse at 20% 80%, rgba(42,168,201,.6), transparent 60%),
      radial-gradient(ellipse at 85% 85%, rgba(42,168,201,.45), transparent 50%),
      linear-gradient(160deg, var(--navy) 0%, #23358a 45%, var(--deep) 100%);
  }
  .brand {
    position: absolute; left: 58px; top: 98px; width: 346px; height: 194px;
    border-radius: 50%; background: var(--navy);
    display: flex; align-items: center; justify-content: center; gap: 12px;
  }
  .brand__dot { width: 22px; height: 22px; border-radius: 50%; background: var(--cyan); }
  .brand__name { font-family: "Kanit", sans-serif; font-style: normal; font-weight: 800; font-size: 44px; color: var(--white); letter-spacing: 1px; }
  .badge-new {
    position: absolute; left: 2px; top: 288px; width: 66px; height: 66px; border-radius: 50%;
    background: #d8eef6; display: flex; align-items: center; justify-content: center;
    transform: rotate(-24deg);
  }
  .badge-new span { font-weight: 800; font-style: italic; font-size: 18px; color: var(--navy); }
  .slogan {
    position: absolute; left: 0; right: 0; top: 352px; text-align: center;
    font-style: italic; font-weight: 800; font-size: 44px;
  }
  .title-band {
    position: absolute; left: 0; right: 0; top: 429px; height: 169px;
    background: linear-gradient(180deg, var(--silver-light) 0%, var(--silver-mid) 50%, var(--silver-light) 100%);
    display: flex; align-items: center; justify-content: center; overflow: hidden;
  }
  .title-band h1 {
    font-family: "Anton", sans-serif; font-weight: 400; font-size: 78px; line-height: 1; color: var(--ink);
    letter-spacing: -1px; transform: scaleY(1.55); white-space: nowrap;
  }
  .uses { position: absolute; left: 8px; right: 8px; top: 617px; height: 189px; display: flex; gap: 10px; }
  .uses__tile { flex: 1; border: 3px solid #bcd8e8; }
  .uses__tile--seats { background: linear-gradient(160deg, #8b929b, #3d434b); }
  .uses__tile--bumper { background: linear-gradient(160deg, #d3202a, #6a0d12 70%, #1a1a1a); }
  .uses__tile--mirror { background: linear-gradient(160deg, #1f3fa0, #5fb7e6); }
  .tagline {
    position: absolute; left: 0; right: 0; top: 826px; text-align: center;
    font-style: italic; font-weight: 700; font-size: 25px; line-height: 1.3;
  }
  .net {
    position: absolute; left: 4px; top: 944px; font-family: "Oswald", sans-serif; line-height: 1.15;
  }
  .net__label { font-weight: 700; font-size: 26px; }
  .net__qty { font-weight: 500; font-size: 20px; }
  .features {
    position: absolute; left: 158px; top: 975px; width: 298px; height: 72px;
    border: 2px solid var(--teal); border-radius: 36px; padding: 9px 0 0 22px;
    font-family: "Oswald", sans-serif; font-weight: 500; font-size: 15px; line-height: 1.25; white-space: nowrap;
  }
</style>
</head>
<body>
  <section class="label">
    <div class="label__art" role="img" aria-label="Swirling blue and teal abstract background"></div>
    <div class="brand"><span class="brand__dot"></span><span class="brand__name">GLOSSWAY</span></div>
    <div class="badge-new"><span>NEW</span></div>
    <p class="slogan">Let It Shine!</p>
    <div class="title-band"><h1>TRIM RESTORER</h1></div>
    <div class="uses">
      <div class="uses__tile uses__tile--seats" role="img" aria-label="Car interior seats"></div>
      <div class="uses__tile uses__tile--bumper" role="img" aria-label="Red car front bumper and headlight"></div>
      <div class="uses__tile uses__tile--mirror" role="img" aria-label="Blue car side mirror"></div>
    </div>
    <p class="tagline">FOR THE EXTERIOR TRIM,<br>RUBBER MOLDINGS, AND VINYL.</p>
    <div class="net">
      <div class="net__label">NET WT</div>
      <div class="net__qty">8 FL OZ (236 mL)</div>
    </div>
    <div class="features">
      Restores Plastic, Rubber and Vinyl<br>
      Seals and Protects Most Hard Surfaces<br>
      UV Protection
    </div>
  </section>
</body>
</html>
```